Automotive spring company needs banner for website

Banner dimensions: 3840 x 880 pixels
Banner need to be consistent with our branding (logo, stationary, colors, fonts, message).
People images should show happiness and it is preferable those people are in or around a car unless it ties into one of the 3 quotes in the must haves below.
Use color blue #4885ed
and gold color #f7d105
Minimal, strong, clean, & tech

Target Market(s)

35-55 male and female

Industry/Entity Type

Auto Repair

Requirements
Must have
• Clickable element for "Shop" or "Make an Appointment"
• "25 Years of Customer Satisfaction" or
• "Get it Done Right by Specialist" or
• "Peace of Mind National Warranty"
• Use our font, Eurostile and/or complimentary font paring

```html
<!DOCTYPE html>
<html lang="en">
<head>
<meta charset="utf-8">
<title>Peace of Mind National Warranty</title>
<link rel="stylesheet" href="https://fonts.googleapis.com/css2?family=Lexend+Exa:wght@600;700&display=swap">
<style>
  :root {
    --cream: #fbf3e2;
    --cream-light: #fdf8ee;
    --ink: #333333;
    --gold: #e0b61f;
    --blue: #4885ed;
    --white: #ffffff;
    --photo-warm: #e9c9a0;
    --photo-sun: #f3dfbf;
    --photo-yellow: #f2c94c;
  }
  * { margin: 0; padding: 0; box-sizing: border-box; }
  html, body { width: 1200px; height: 275px; overflow: hidden; background: var(--cream); }
  .banner {
    position: relative;
    width: 1200px;
    height: 275px;
    overflow: hidden;
    background: linear-gradient(90deg, var(--cream) 0%, var(--cream-light) 70%, var(--cream) 100%);
    font-family: "Lexend Exa", "Arial Black", sans-serif;
  }
  .hero-photo {
    position: absolute;
    left: 0;
    top: 0;
    width: 590px;
    height: 270px;
    background:
      radial-gradient(ellipse 220px 120px at 300px 150px, var(--photo-yellow) 0%, rgba(242,201,76,0) 100%),
      linear-gradient(180deg, var(--photo-sun) 0%, var(--photo-warm) 60%, #d8d4cc 100%);
    -webkit-mask-image: linear-gradient(90deg, #000 0%, #000 75%, transparent 100%);
    mask-image: linear-gradient(90deg, #000 0%, #000 75%, transparent 100%);
  }
  .headline {
    position: absolute;
    right: 38px;
    top: 62px;
    text-align: right;
    color: var(--ink);
    font-size: 38px;
    line-height: 44px;
    font-weight: 700;
    letter-spacing: -1px;
    text-transform: uppercase;
    white-space: nowrap;
  }
  .cta {
    position: absolute;
    right: 262px;
    top: 214px;
    height: 36px;
    padding: 0 20px;
    display: flex;
    align-items: center;
    background: var(--blue);
    color: var(--white);
    font-size: 13px;
    font-weight: 600;
    letter-spacing: 1px;
    text-transform: uppercase;
    text-decoration: none;
  }
  .brand {
    position: absolute;
    right: 38px;
    top: 212px;
    height: 40px;
    display: flex;
    align-items: center;
    gap: 10px;
    color: var(--gold);
    font-size: 26px;
    font-weight: 700;
    letter-spacing: -1px;
    text-transform: uppercase;
  }
  .brand-mark {
    width: 14px;
    height: 14px;
    background: var(--gold);
  }
  .base-band {
    position: absolute;
    left: 0;
    bottom: 0;
    width: 1200px;
    height: 5px;
    background: var(--blue);
  }
</style>
</head>
<body>
  <div class="banner">
    <div class="hero-photo" role="img" aria-label="Happy woman in a yellow shirt standing in a white convertible with arms spread wide in warm sunlight"></div>
    <h1 class="headline">Peace of Mind<br>National Warranty</h1>
    <a class="cta" href="#appointment">Make an Appointment</a>
    <div class="brand">
      <span class="brand-mark"></span>
      <span class="brand-name">Truecoil</span>
    </div>
    <div class="base-band"></div>
  </div>
</body>
</html>
```